Chutney and Jam Manufacturer needs a label for Jar.

We would like a label designed for a new Christmas Jars called Bartolds Bright Fire Pickle and Weltons Dawn Cordial. The retailers we are targeting are Garden Centres, farm shops and independent retail. Although in some ways not relevant some of the Christmas beer labels carry some form of theme we are looking for. Its fun and festive and not an all year around serious product. That said please note our target market.
The label will be approximately 90mm wide x 55mm height.
Picture of the Jar provided.

Target Market(s)

Predominantly female 40+ due to outlet supplied. But this is not paramount to the design.

Industry/Entity Type

Home And Garden

Requirements
Must have
• Clear design on shelf of what it is - remember this is to go on glass jars.
• Shelf impact and clarity
• The design feel is in the name of the product. Bartolds Bright Fire Pickle and Weltons Dawn Cordial
Nice to have
• Fun and quirky but again not essential.
Should not have
• The Brand is Quillet Foods but this is not important on this concept. We will add in the logo if we have room and it fits in with the selected design.

```html
<!DOCTYPE html>
<html lang="en">
<head>
<meta charset="utf-8">
<title>Bartolds Bright Fire Pickle – Jar Label</title>
<link rel="stylesheet" href="https://fonts.googleapis.com/css2?family=Oswald:wght@500;600&family=Montserrat:wght@700&display=swap">
<style>
  :root {
    --page-bg: #ececec;
    --label-red: #d2301f;
    --label-red-deep: #b8231a;
    --label-red-light: #e8492c;
    --ink-white: #ffffff;
    --ink-cream: #f4e6bf;
    --ribbon-white: #fbf8f4;
    --ribbon-shadow: #d9d2cc;
    --ribbon-text: #b3261b;
    --art-white: rgba(255, 255, 255, 0.82);
  }
  html, body {
    margin: 0;
    padding: 0;
    width: 1080px;
    height: 1200px;
    overflow: hidden;
    background: var(--page-bg);
  }
  .canvas {
    position: relative;
    width: 1080px;
    height: 1200px;
  }
  .label {
    position: absolute;
    left: 201px;
    top: 100px;
    width: 678px;
    height: 1000px;
    border-radius: 12px;
    background: var(--label-red-deep);
    box-shadow: 0 10px 30px rgba(0, 0, 0, 0.18);
    overflow: hidden;
  }
  .label-field {
    position: absolute;
    inset: 30px;
    background: radial-gradient(ellipse at 50% 45%, var(--label-red-light) 0%, var(--label-red) 70%);
  }
  .label-frame {
    position: absolute;
    inset: 44px;
    border: 2px dotted rgba(255, 255, 255, 0.75);
  }
  .corner-ornament {
    position: absolute;
    width: 40px;
    height: 40px;
    background: rgba(255, 255, 255, 0.35);
    border-radius: 4px;
  }
  .corner-ornament.tl { left: 24px; top: 24px; }
  .corner-ornament.tr { right: 24px; top: 24px; }
  .corner-ornament.bl { left: 24px; bottom: 24px; }
  .corner-ornament.br { right: 24px; bottom: 24px; }
  .village-skyline {
    position: absolute;
    left: 102px;
    top: 81px;
    width: 476px;
    height: 56px;
    background: linear-gradient(to bottom, rgba(255,255,255,0.15), var(--art-white));
    border-radius: 4px;
  }
  .mascot {
    position: absolute;
    left: 262px;
    top: 152px;
    width: 150px;
    height: 212px;
    border-radius: 50% 50% 45% 45%;
    background: radial-gradient(circle at 50% 55%, #ffffff 0%, #f1e2d6 55%, #e04a32 100%);
  }
  .line-art {
    position: absolute;
    inset: 0;
  }
  .product-name {
    position: absolute;
    inset: 0;
    margin: 0;
    text-align: center;
    font-family: 'Oswald', sans-serif;
    text-transform: uppercase;
    line-height: 1;
  }
  .product-name span {
    position: absolute;
    left: 0;
    right: 0;
    display: block;
  }
  .product-name .maker {
    top: 404px;
    font-size: 84px;
    font-weight: 500;
    color: var(--ink-white);
    letter-spacing: 1px;
  }
  .product-name .variety {
    top: 500px;
    font-size: 92px;
    font-weight: 600;
    color: var(--ink-cream);
    letter-spacing: -1px;
  }
  .product-name .kind {
    top: 602px;
    font-size: 112px;
    font-weight: 600;
    color: var(--ink-cream);
  }
  .tagline {
    position: absolute;
    left: 0;
    right: 0;
    top: 776px;
    margin: 0;
    text-align: center;
    font-family: 'Montserrat', sans-serif;
    font-weight: 700;
    font-size: 23px;
    letter-spacing: 1px;
    color: var(--ribbon-text);
    text-transform: uppercase;
  }
  .flourish {
    position: absolute;
    left: 230px;
    top: 843px;
    width: 218px;
    height: 32px;
    background: linear-gradient(to right, transparent, var(--art-white), transparent);
    border-radius: 16px;
  }
  .sleigh-team {
    position: absolute;
    left: 137px;
    top: 912px;
    width: 413px;
    height: 48px;
    background: linear-gradient(to right, var(--art-white), rgba(255,255,255,0.25));
    border-radius: 4px;
  }
</style>
</head>
<body>
<main class="canvas">
  <article class="label">
    <div class="label-field"></div>
    <div class="label-frame"></div>
    <div class="corner-ornament tl" role="img" aria-label="Corner flourish ornament"></div>
    <div class="corner-ornament tr" role="img" aria-label="Corner flourish ornament"></div>
    <div class="corner-ornament bl" role="img" aria-label="Corner flourish ornament"></div>
    <div class="corner-ornament br" role="img" aria-label="Corner flourish ornament"></div>

    <div class="village-skyline" role="img" aria-label="White silhouette of a snowy village with church and fir trees"></div>
    <div class="mascot" role="img" aria-label="Cartoon festive mascot head with a red bobble hat"></div>

    <svg class="line-art" width="678" height="1000" viewBox="0 0 678 1000" aria-hidden="true">
      <g fill="none" stroke="var(--ink-cream)" stroke-width="2.5" stroke-linecap="round">
        <path d="M 255 300 Q 140 330 112 400 Q 96 440 112 480"/>
        <path d="M 423 300 Q 538 330 566 400 Q 582 440 566 480"/>
        <line x1="84" y1="548" x2="118" y2="568"/>
        <line x1="70" y1="612" x2="122" y2="612"/>
        <line x1="84" y1="676" x2="118" y2="656"/>
        <line x1="594" y1="548" x2="560" y2="568"/>
        <line x1="608" y1="612" x2="556" y2="612"/>
        <line x1="594" y1="676" x2="560" y2="656"/>
      </g>
      <g>
        <polygon points="92,800 130,776 130,832 104,832 118,816" fill="var(--ribbon-shadow)"/>
        <polygon points="586,800 548,776 548,832 574,832 560,816" fill="var(--ribbon-shadow)"/>
        <path d="M 118 766 Q 339 748 560 766 L 560 818 Q 339 800 118 818 Z" fill="var(--ribbon-white)"/>
      </g>
    </svg>

    <h1 class="product-name">
      <span class="maker">Bartolds</span>
      <span class="variety">Bright Fire</span>
      <span class="kind">Pickle</span>
    </h1>

    <p class="tagline">Made for the feast</p>

    <div class="flourish" role="img" aria-label="Small decorative scroll flourish"></div>
    <div class="sleigh-team" role="img" aria-label="White silhouette of reindeer pulling a sleigh"></div>
  </article>
</main>
</body>
</html>
```